VelMarkory-Tagsworthly Partial Redesign - Web App

Are you able to apply your creativity to an existing layout? I’m convinced that even just a few touches can make a big difference to add personality and professionalism to a website design, and I’m looking for someone able to use existing ideas and bring them to the next level while keeping inside some given constraints.
The actual job is to improve an existing design concept and to apply it creatively to a landing page, a simple home page, and an older web app (single page website).
To help you start with a clear picture of the current situation and of my requirements, I created a detailed brief with screenshots, live examples, and complete instructions. You can find it attached to this job.
My tastes are inclined towards clean and simple designs. For this project I'm not looking for dazzling novelty, but for very solid craftsmanship. Are the right man - or woman - for the job?
Updates
I wanted to thank everybody who participated in this project. I made a choice, but also other designs were interesting. Hope to work with you another time.
Target Market(s)
Our main target is social media marketers and startuppers
Look and feel
Each slider illustrates characteristics of the customer's brand and the style your logo design should communicate.

```html
<!DOCTYPE html>
<html lang="en">
<head>
<meta charset="utf-8">
<title>VelMarkory – CyberSocial Branding Intelligence</title>
<link href="https://fonts.googleapis.com/css2?family=Arimo:wght@400;700&family=Ubuntu:wght@400;700&display=swap" rel="stylesheet">
<style>
:root{
  --nav-dark:#151515;
  --nav-text:#d8d8d8;
  --hero-deep:#0d3d87;
  --hero-mid:#1f63b3;
  --hero-light:#3d86d0;
  --white:#ffffff;
  --arrow-green:#2fd84a;
  --cta-top:#27e6ff;
  --cta-bottom:#00b4e0;
  --cta-text:#0b3c5c;
  --footer-bg:#1b1b1b;
  --footer-line:#3a3a3a;
  --footer-text:#e6e6e6;
  --muted:#8a8a8a;
  --field-bg:#232323;
  --accent-blue:#3a8fd8;
  --send-blue:#1e6fc2;
  --app-bar:#2c2c2c;
  --app-link:#2a7ad4;
}
*{margin:0;padding:0;box-sizing:border-box}
html,body{width:1200px;height:831px;overflow:hidden;background:var(--footer-bg)}
body{position:relative;font-family:Arimo,Arial,sans-serif;color:var(--white)}
.abs{position:absolute}

.topnav{left:0;top:0;width:1200px;height:43px;background:linear-gradient(#2a2a2a,var(--nav-dark));border-bottom:1px solid #000}
.topnav a{position:absolute;top:14px;font:700 12px Arimo,Arial,sans-serif;color:var(--nav-text);text-decoration:none}
.topnav .active{top:4px;left:366px;width:95px;height:35px;border-radius:7px;background:#0c0c0c;border:1px solid #444;color:var(--white);padding:10px 0 0 18px}
.topnav .active::after{content:"";position:absolute;left:75px;top:15px;border:5px solid transparent;border-top:6px solid var(--white)}

.hero{left:0;top:43px;width:1200px;height:464px;background:radial-gradient(ellipse 70% 90% at 50% 10%,var(--hero-light),var(--hero-mid) 45%,var(--hero-deep));}
.brand{left:430px;top:73px;display:flex;align-items:center;gap:18px}
.brand-dot{width:60px;height:60px;border-radius:50%;background:var(--white)}
.brand-name{font:700 56px/1 Ubuntu,sans-serif;letter-spacing:-1px}
.tagline{left:560px;top:132px;font:400 18px Ubuntu,sans-serif}

.features{left:224px;top:221px;list-style:none}
.features li{height:32px;display:flex;align-items:center;font-size:13.6px}
.features svg{margin-right:11px}
.cta{left:320px;top:376px;width:164px;height:40px;background:linear-gradient(var(--cta-top),var(--cta-bottom));border-radius:2px;box-shadow:0 12px 10px -8px rgba(0,0,0,.45);font:700 16px/40px Arimo,sans-serif;color:var(--cta-text);text-align:center;letter-spacing:.3px}

.appshot{left:616px;top:199px;width:361px;height:242px;background:var(--white);border:1px solid #999;box-shadow:0 40px 30px -20px rgba(0,0,0,.45);overflow:hidden;color:#333}
.app-bar{height:24px;background:var(--app-bar);position:relative}
.app-bar span{position:absolute;top:5px;height:14px;border:1px solid #555;border-radius:2px;background:#1a1a1a;color:#ddd;font:700 6px/12px Arimo,sans-serif;padding:0 6px}
.app-head{height:56px;background:linear-gradient(#fff,#eee);border-bottom:1px solid #ccc;padding:9px 16px}
.app-title{font:400 13px Ubuntu,sans-serif}
.app-title b{font-weight:400;color:var(--app-link);font-size:14px}
.app-title small{font:italic 6px Arimo,sans-serif;color:#888}
.app-title small i{color:var(--app-link)}
.tabs{margin-top:9px;display:flex;gap:7px}
.tabs span{font:700 5.5px/12px Arimo,sans-serif;border:1px solid #bbb;border-radius:7px;padding:0 8px;background:#fff}
.tabs .on{color:var(--app-link)}
.app-sub{left:16px;top:96px;font:400 11px Ubuntu,sans-serif}
.app-controls{left:0;bottom:0;width:361px;height:24px;background:linear-gradient(#555,#2a2a2a)}

.divider{left:0;top:507px;width:1200px;height:3px;background:#777}
.col-title{top:527px;font:400 18px Arimo,sans-serif;color:var(--footer-text);width:230px;padding-bottom:10px;border-bottom:1px solid var(--footer-line)}
.reach{left:228px;top:576px;list-style:none;font-size:12px;color:var(--footer-text)}
.reach li{height:24px;display:flex;align-items:center;padding-left:28px;position:relative}
.reach svg,.reach .sq{position:absolute;left:0}
.reach .sq{width:11px;height:11px;background:#ddd;left:3px}
.reach .ci{width:11px;height:11px;background:#ddd;border-radius:50%;left:3px}
.about-text{left:482px;top:569px;width:228px;font-size:11.4px;line-height:17.6px;letter-spacing:.5px;color:#d0d0d0}
.about-dot{float:left;width:40px;height:40px;border-radius:50%;border:1px solid #bbb;margin:10px 50px 6px 18px}
.field{left:744px;width:233px;background:var(--field-bg);border-radius:3px;box-shadow:inset 0 3px 6px rgba(0,0,0,.6);font-size:10px;color:#ddd;padding:8px 15px}
.req{left:748px;top:749px;font-size:10px;color:var(--accent-blue)}
.send{left:925px;top:746px;width:50px;height:18px;background:linear-gradient(#2e86db,var(--send-blue));border:1px solid #5aa3e8;border-radius:2px;font-size:10px;line-height:16px;text-align:center}
.bottom{left:0;top:791px;width:1200px;height:40px;border-top:1px solid #000;background:#1e1e1e;font-size:8.5px;color:var(--muted)}
.bottom .copy{position:absolute;left:226px;top:17px}
.bottom .links{position:absolute;right:222px;top:17px}
.bottom .links span{margin:0 6px}
</style>
</head>
<body>
<nav class="abs topnav">
  <a style="left:249px">Home</a>
  <a style="left:315px">About</a>
  <a class="active">Products</a>
  <a style="left:478px">Blog</a>
</nav>

<header class="abs hero"></header>
<div class="abs brand"><span class="brand-dot"></span><span class="brand-name">VelMarkory</span></div>
<div class="abs tagline">CyberSocial Branding Intelligence</div>

<ul class="abs features">
  <li><svg width="20" height="18" viewBox="0 0 20 18"><path d="M0 6h10V0l10 9-10 9v-6H0z" fill="var(--arrow-green)"/></svg>Discover and track&nbsp;<b>trend</b>&nbsp;as they develop</li>
  <li><svg width="20" height="18" viewBox="0 0 20 18"><path d="M0 6h10V0l10 9-10 9v-6H0z" fill="var(--arrow-green)"/></svg>Learn everything about up to&nbsp;<b>50 top influencers</b></li>
  <li><svg width="20" height="18" viewBox="0 0 20 18"><path d="M0 6h10V0l10 9-10 9v-6H0z" fill="var(--arrow-green)"/></svg>Evaluate and compare about&nbsp;<b>your own influencers</b></li>
  <li><svg width="20" height="18" viewBox="0 0 20 18"><path d="M0 6h10V0l10 9-10 9v-6H0z" fill="var(--arrow-green)"/></svg>Read the&nbsp;<b>actual tweets</b>&nbsp;where influence is exercised</li>
</ul>
<div class="abs cta">REGISTER NOW</div>

<section class="abs appshot">
  <div class="app-bar">
    <span style="left:18px">&#8962;</span><span style="left:44px">Products ▾</span>
    <span style="left:314px">Blog</span><span style="left:342px">Abo</span>
  </div>
  <div class="app-head">
    <div class="app-title">Hashtag: <b>#socialtips</b> <small>Tracked influencers: <i>@jonaswell</i>, <i>@redfoxmedia</i></small></div>
    <div class="tabs"><span>Summary</span><span>Timeline</span><span class="on">Influencers</span><span>Hashtags</span></div>
  </div>
  <div class="abs app-sub">Hashtag Top Influencers</div>
  <svg class="abs" style="left:20px;top:126px" width="340" height="92" viewBox="0 0 340 92">
    <text x="2" y="4" font-size="6" fill="#333" font-family="Arimo">1. socialbiz</text>
    <text x="30" y="13" font-size="4.5" font-weight="700" fill="#333" font-family="Arimo">Top Influencers Reach Share</text>
    <circle cx="62" cy="45" r="30" fill="#2f5fc8"/>
    <path d="M62 45L32 45A30 30 0 0 1 54 16Z" fill="#d9351d"/>
    <text x="40" y="35" font-size="4.5" fill="#fff" font-family="Arimo">27.9%</text>
    <text x="66" y="60" font-size="4.5" fill="#fff" font-family="Arimo">72.1%</text>
    <rect x="100" y="10" width="4" height="4" fill="#2f5fc8"/><text x="107" y="14" font-size="4.5" fill="#333" font-family="Arimo">Top 10</text>
    <rect x="100" y="18" width="4" height="4" fill="#d9351d"/><text x="107" y="22" font-size="4.5" fill="#333" font-family="Arimo">Others</text>
    <line x1="195" y1="-8" x2="195" y2="92" stroke="#333"/>
    <text transform="translate(188 70) rotate(-90)" font-size="6" fill="#333" font-family="Arimo">ence for this campaign</text>
    <circle cx="233" cy="12" r="22" fill="#ccc"/>
    <circle cx="232" cy="86" r="18" fill="#ccc"/>
  </svg>
  <div class="abs app-controls">
    <svg width="361" height="24" viewBox="0 0 361 24">
      <path d="M13 7l9 5-9 5z" fill="#ddd"/>
      <rect x="42" y="10" width="224" height="5" rx="2.5" fill="#777"/>
      <rect x="42" y="10" width="110" height="5" rx="2.5" fill="#e64a4a"/>
      <circle cx="151" cy="12.5" r="4" fill="#ddd"/>
      <text x="273" y="15" font-size="7" fill="#ccc" font-family="Arimo">3.47 / 9.29</text>
      <path d="M333 9h4l4-3v13l-4-3h-4z" fill="#ccc"/>
      <rect x="353" y="8" width="6" height="8" fill="none" stroke="#ccc"/>
    </svg>
  </div>
</section>

<div class="abs divider"></div>

<h2 class="abs col-title" style="left:228px">Reach Us</h2>
<h2 class="abs col-title" style="left:486px">About Us</h2>
<h2 class="abs col-title" style="left:744px">Contact Us</h2>

<ul class="abs reach">
  <li><svg width="17" height="12" viewBox="0 0 17 12"><rect width="17" height="12" fill="#ddd"/><path d="M0 0l8.5 7L17 0" stroke="#1b1b1b" fill="none"/></svg>info@velmarkory.com</li>
  <li><svg width="14" height="14" viewBox="0 0 14 14"><path d="M3 1l3 3-2 2c1 2 2 3 4 4l2-2 3 3-2 2C6 13 1 8 1 3z" fill="#ddd"/></svg>123-456-7890</li>
  <li><svg width="16" height="14" viewBox="0 0 16 14"><path d="M8 0l8 7h-2v7H10V9H6v5H2V7H0z" fill="#ddd"/></svg>Somewhere street 12</li>
  <li>City Name</li>
  <li>Country Name, 12345</li>
  <li><span class="ci"></span>@velmarkory</li>
  <li><span class="sq"></span>linkpage.net/velmarkory</li>
</ul>

<p class="abs about-text"><span class="about-dot"></span>Lorem ipsum dolor sit amet, consectetuer adipiscing elit, sed diam nonummy nibh euismod Lorem ipsum dolor sit amet, consectetuer adipiscing elit, sed diam nonummy nibh euismod tincidunt ut laoreet dolore magna aliquam erat volutpat. Ut wisi enim ad minim veniam, quis nostrud exerci tation ullamcor-per suscipit lobortis nisl ut aliquip ex ea</p>

<div class="abs field" style="top:572px;height:26px">your name</div>
<div class="abs field" style="top:606px;height:26px">your email</div>
<div class="abs field" style="top:642px;height:99px">your message</div>
<div class="abs req">* All Fields Are Required</div>
<div class="abs send">SEND</div>

<footer class="abs bottom">
  <span class="copy">Copyright @ 2012 VelMarkory</span>
  <span class="links">About Us<span>|</span>Programs<span>|</span>Services<span>|</span>Contact</span>
</footer>
</body>
</html>
```